Indie musician needs album cover art

I am an independant musician releasing my second album via digital sources. I plan to make it available on Vendly and other digital stores but primarily distribute it free through Tunegrove.

The album's music style is a blend of singer-songwriter folk, punk, alt country, electronic rock and spoken word. The lyrical content is a dark journey through travel in foreign countries, relationships, airports and theatres, formed during my own journey as an audio engineer for a travelling theatre show.

The album is called "Ash Under Glass" - at times both a plea and a directive. I would like the album cover to reflect a sense of longing, restlessness, unease and movement. A subversive tone is also possible.

I have had a go at designing a couple of ideas myself, using my own photos. I like the ideas but I am not skilled in graphic design and am unable to take them further to get the right feel and look. I will post these as examples of tone. The finished work does not need to copy either of these.

A .zip of the album can be downloaded here (low fi mp3):

http://fylo.io/Qx7rT4

Target Market(s)

People who enjoy thoughtful, honest, homemade music. Definitely not a teeny pop audience. Adult, subversive, educated, emotional...

Industry/Entity Type

Graphic Design

Requirements
Must have
• Artist name (no caps): kipwren
Album name (prefer no caps): ash under glass

```html
<!DOCTYPE html>
<html lang="en">
<head>
<meta charset="utf-8">
<title>kipwren — ash under glass</title>
<link rel="stylesheet" href="https://fonts.googleapis.com/css2?family=Michroma&family=Playfair+Display:ital@1&display=swap">
<style>
  :root {
    --bg: #000000;
    --ink: #f2f2f2;
    --balloon-pink: #d8355a;
    --balloon-teal: #3fc7b4;
    --balloon-lime: #b8f04a;
    --balloon-navy: #1f2f8a;
    --balloon-cream: #e9c9a8;
  }
  html, body {
    margin: 0;
    padding: 0;
    width: 1200px;
    height: 1200px;
    overflow: hidden;
    background: var(--bg);
  }
  .cover {
    position: relative;
    width: 1200px;
    height: 1200px;
    background: var(--bg);
  }
  .balloon-art {
    position: absolute;
    left: 100px;
    top: 90px;
    width: 640px;
    height: 1060px;
  }
  .artist-name {
    position: absolute;
    left: 728px;
    top: 780px;
    margin: 0;
    font-family: "Michroma", sans-serif;
    font-weight: 400;
    font-size: 60px;
    letter-spacing: 4px;
    line-height: 1;
    color: var(--ink);
  }
  .album-title {
    position: absolute;
    left: 712px;
    top: 862px;
    margin: 0;
    font-family: "Playfair Display", serif;
    font-style: italic;
    font-size: 46px;
    letter-spacing: 2px;
    line-height: 1;
    color: var(--ink);
  }
</style>
</head>
<body>
  <main class="cover">
    <svg class="balloon-art" viewBox="0 0 640 1060" role="img" aria-label="Photograph of a person carrying a huge bundle of colourful cartoon-character balloons, with a faint reflection below">
      <defs>
        <radialGradient id="bundle" cx="50%" cy="40%" r="55%">
          <stop offset="0%" stop-color="var(--balloon-cream)"/>
          <stop offset="35%" stop-color="var(--balloon-pink)"/>
          <stop offset="65%" stop-color="var(--balloon-teal)"/>
          <stop offset="100%" stop-color="var(--balloon-navy)" stop-opacity="0"/>
        </radialGradient>
        <radialGradient id="reflection" cx="50%" cy="50%" r="50%">
          <stop offset="0%" stop-color="var(--balloon-pink)" stop-opacity="0.25"/>
          <stop offset="100%" stop-color="var(--balloon-pink)" stop-opacity="0"/>
        </radialGradient>
      </defs>
      <ellipse cx="320" cy="420" rx="320" ry="420" fill="url(#bundle)"/>
      <ellipse cx="290" cy="130" rx="90" ry="90" fill="var(--balloon-lime)" opacity="0.6"/>
      <ellipse cx="400" cy="960" rx="300" ry="90" fill="url(#reflection)"/>
    </svg>
    <h1 class="artist-name">kipwren</h1>
    <p class="album-title">ash under glass</p>
  </main>
</body>
</html>
```